Security Business card

I need a new business card for my new company Bastion Crest Security Group we provide security for clubs,pubs,hotels etc. I would like to see the main colors red and black to be used. The final design should communicate honor and integrity.

Industry/Entity Type

Security

Contact Information for Business Card

Marcus Delvane
Company Name-Bastion Crest Security Group
Abn-47318265094
Acn-318265094
address- po box 7352 Ferndale nsw 2291
phone- 0437682915
email- Marcus@bastioncrest.com.au

```html
<!DOCTYPE html>
<html lang="en">
<head>
<meta charset="utf-8">
<title>Bastion Crest Security Group – Business Card</title>
<link rel="stylesheet" href="https://fonts.googleapis.com/css2?family=Open+Sans:wght@400&display=swap">
<style>
  :root {
    --card-black: #000000;
    --crest-red: #8a0b0b;
    --crest-red-dark: #5c0606;
    --text-white: #ffffff;
    --rule-light: #e6e6e6;
    --rule-grey: #7a7a7a;
  }
  * { margin: 0; padding: 0; box-sizing: border-box; }
  html, body {
    width: 1200px;
    height: 740px;
    overflow: hidden;
    background: var(--card-black);
  }
  .card {
    position: relative;
    width: 1200px;
    height: 740px;
    background: var(--card-black);
    color: var(--text-white);
    font-family: "Open Sans", Arial, sans-serif;
    font-weight: 400;
  }
  .brand-mark {
    position: absolute;
    left: 68px;
    top: 55px;
    width: 340px;
    height: 340px;
  }
  .company-name {
    position: absolute;
    left: 482px;
    top: 172px;
    font-size: 45px;
    line-height: 1;
    letter-spacing: 0.2px;
    white-space: nowrap;
  }
  .rule {
    position: absolute;
    height: 3px;
    background: linear-gradient(90deg, var(--rule-grey), var(--rule-light) 40%, var(--rule-light) 70%, var(--rule-grey));
  }
  .rule--heading { left: 471px; top: 236px; width: 660px; }
  .rule--footer { left: 51px; top: 633px; width: 1097px; }
  .icon {
    position: absolute;
    fill: var(--crest-red);
  }
  .icon--person { left: 482px; top: 257px; width: 79px; height: 95px; }
  .icon--phone { left: 68px; top: 442px; width: 66px; height: 62px; }
  .icon--mail { left: 482px; top: 434px; width: 79px; height: 70px; }
  .icon--office { left: 70px; top: 532px; width: 71px; height: 77px; }
  .detail {
    position: absolute;
    font-size: 38px;
    line-height: 1;
    white-space: nowrap;
  }
  .detail--name { left: 592px; top: 299px; }
  .detail--phone { left: 175px; top: 456px; }
  .detail--email { left: 592px; top: 456px; font-size: 37px; }
  .detail--address { left: 175px; top: 561px; }
  .registration {
    position: absolute;
    top: 645px;
    font-size: 38px;
    line-height: 1;
    white-space: nowrap;
  }
  .registration--abn { left: 54px; }
  .registration--acn { right: 54px; }
</style>
</head>
<body>
<div class="card">

  <svg class="brand-mark" viewBox="0 0 340 340" role="img" aria-label="Company crest mark area">
    <defs>
      <radialGradient id="crestFill" cx="50%" cy="45%" r="55%">
        <stop offset="0%" stop-color="#8a0b0b"/>
        <stop offset="100%" stop-color="#3a0404"/>
      </radialGradient>
    </defs>
    <circle cx="170" cy="170" r="165" fill="url(#crestFill)"/>
  </svg>

  <h1 class="company-name">Bastion Crest Security Group</h1>
  <div class="rule rule--heading"></div>

  <svg class="icon icon--person" viewBox="0 0 80 96" aria-hidden="true">
    <ellipse cx="40" cy="26" rx="20" ry="24"/>
    <path d="M0 96 V78 C0 62 14 52 28 50 L40 58 L52 50 C66 52 80 62 80 78 V96 Z"/>
    <path d="M36 58 L44 58 L46 86 L40 94 L34 86 Z" fill="#ffffff"/>
  </svg>
  <p class="detail detail--name">Marcus Delvane</p>

  <svg class="icon icon--phone" viewBox="0 0 66 62" aria-hidden="true">
    <path d="M14 2 L24 16 C26 19 25 22 22 24 L18 27 C22 36 30 44 39 48 L42 44 C44 41 47 40 50 42 L64 52 C66 54 66 57 63 59 L58 61 C44 64 2 34 2 12 L4 6 C6 2 10 0 14 2 Z" fill="none" stroke="var(--crest-red)" stroke-width="5"/>
    <path d="M10 6 L20 18 L14 24 C12 18 10 12 10 6 Z"/>
    <path d="M44 50 L58 56 L52 58 C49 56 46 53 44 50 Z"/>
  </svg>
  <p class="detail detail--phone">0437682915</p>

  <svg class="icon icon--mail" viewBox="0 0 80 70" aria-hidden="true">
    <path d="M40 0 L80 28 V70 H0 V28 Z"/>
    <path d="M14 30 L40 14 L66 30 L40 46 Z" fill="#ffffff"/>
    <path d="M8 38 L30 52 L8 64 Z M72 38 L50 52 L72 64 Z" fill="#ffffff"/>
  </svg>
  <p class="detail detail--email">Marcus@bastioncrest.com.au</p>

  <svg class="icon icon--office" viewBox="0 0 72 78" aria-hidden="true">
    <path d="M0 0 H72 V78 H0 Z M10 8 V70 H28 V58 H44 V70 H62 V8 Z" fill="var(--crest-red)"/>
    <rect x="4" y="4" width="64" height="70" fill="#1a0000"/>
    <g fill="#ffffff">
      <rect x="14" y="12" width="10" height="8"/><rect x="31" y="12" width="10" height="8"/><rect x="48" y="12" width="10" height="8"/>
      <rect x="14" y="25" width="10" height="8"/><rect x="31" y="25" width="10" height="8"/><rect x="48" y="25" width="10" height="8"/>
      <rect x="14" y="38" width="10" height="8"/><rect x="31" y="38" width="10" height="8"/><rect x="48" y="38" width="10" height="8"/>
      <rect x="14" y="51" width="10" height="8"/><rect x="48" y="51" width="10" height="8"/>
    </g>
    <rect x="30" y="56" width="12" height="18" fill="var(--crest-red)"/>
  </svg>
  <p class="detail detail--address">P.O. Box 7352 Ferndale NSW 2291</p>

  <div class="rule rule--footer"></div>
  <p class="registration registration--abn">Abn-47318265094</p>
  <p class="registration registration--acn">Acn-318265094</p>

</div>
</body>
</html>
```